Dale Hornsby's Swingcraft Big Band — Hot & Sticky ------ CD Cover Art (and Disc Art)

Need a front cover jacket and a disc design for a fantastic all-pro big band (jazz/funk/reggae) CD. We really want to use a group photo somehow since so many of the band members are world famous, LA's finest studio musicians with mostly original music arranged by the biggest names in jazz. Playful, fun, lighthearted, tasteful arrangements with world class soloists.

Target Market(s)

Music/Jazz/Big band enthusiasts; other musicians

Other font styles liked:
• See uploaded file #4

Colors

Designer to choose colors to be used in the design.

Requirements
Must have
• Legibility . . . must be easy to read and not crowded or cluttered. Font idea below (A Quiet Night Beneath The Tangled Pines) is for feel and flavor. It is absolutely not necessary to match if you have something you like better.
Nice to have
• Colorful but not tacky. Maybe a play on the CD title, Hot and Sticky?

```html
<!DOCTYPE html>
<html lang="en">
<head>
<meta charset="utf-8">
<title>Dale Hornsby's Swingcraft Big Band — Hot and Sticky</title>
<link href="https://fonts.googleapis.com/css2?family=Sorts+Mill+Goudy&family=Ultra&family=Archivo+Black&display=swap" rel="stylesheet">
<style>
  :root {
    --page: #ffffff;
    --ink: #000000;
    --paper: #ffffff;
    --title-blue: #2ba4e0;
    --photo-warm: #6b5446;
    --photo-mid: #3a2e28;
  }
  html, body {
    margin: 0;
    padding: 0;
    width: 1200px;
    height: 1200px;
    overflow: hidden;
    background: var(--page);
  }
  .cover {
    position: absolute;
    left: 87px;
    top: 87px;
    width: 1026px;
    height: 1026px;
    background: var(--ink);
    outline: 1px solid #e6e6e6;
    overflow: hidden;
  }
  .title-band {
    position: absolute;
    left: 0;
    top: 0;
    width: 100%;
    height: 106px;
    background: var(--paper);
    display: flex;
    align-items: center;
    justify-content: center;
  }
  .band-name {
    margin: 0;
    font-family: "Sorts Mill Goudy", Georgia, serif;
    font-weight: 400;
    font-size: 57px;
    letter-spacing: 0.5px;
    color: var(--title-blue);
    white-space: nowrap;
  }
  .group-photo {
    position: absolute;
    left: 0;
    top: 392px;
    width: 100%;
    height: 530px;
    background:
      radial-gradient(ellipse at 50% 30%, rgba(150,120,100,0.55), transparent 60%),
      linear-gradient(to bottom, var(--photo-warm) 0%, var(--photo-mid) 70%, var(--ink) 100%);
  }
  .album-title {
    position: absolute;
    left: 0;
    top: 0;
    width: 1026px;
    height: 1026px;
  }
  .album-title text {
    fill: var(--paper);
    font-family: "Ultra", "Rockwell", serif;
  }
  .disc-format,
  .label-name {
    position: absolute;
    font-family: "Archivo Black", Arial, sans-serif;
    color: var(--paper);
    line-height: 1;
  }
  .disc-format {
    left: 29px;
    top: 940px;
    font-size: 15px;
    letter-spacing: 0.5px;
  }
  .label-name {
    right: 29px;
    top: 953px;
    font-size: 18px;
    text-align: right;
  }
</style>
</head>
<body>
  <main class="cover">
    <header class="title-band">
      <h1 class="band-name">Dale Hornsby's Swingcraft Big Band</h1>
    </header>

    <div class="group-photo" role="img" aria-label="Group photo of the big band members standing and seated with their horns in a recording studio"></div>

    <svg class="album-title" viewBox="0 0 1026 1026" aria-label="Hot and Sticky">
      <text x="33" y="489" font-size="500" textLength="872" lengthAdjust="spacingAndGlyphs">HOT</text>
      <text transform="translate(930 141) rotate(90)" font-size="104" textLength="260" lengthAdjust="spacingAndGlyphs">and</text>
      <text x="33" y="897" font-size="272" textLength="976" lengthAdjust="spacingAndGlyphs">STICKY</text>
    </svg>

    <div class="disc-format">STEREO DISC<br>AUDIO</div>
    <div class="label-name">BLUEWATER<br>RECORDS</div>
  </main>
</body>
</html>
```